Thank you cards for online orders

We have a logo that is attached and I'd for it to be used to make a thank you card that will give our clients some info on product care as well as refund/exchange policy. so maybe a small package that includes a thank you card, and policy details
Updates

Sick

Target Market(s)

Females for 20-70

```html
<!DOCTYPE html>
<html lang="en">
<head>
<meta charset="utf-8">
<title>Bellara – Thank You Card</title>
<link rel="stylesheet" href="https://fonts.googleapis.com/css2?family=Raleway:wght@400;500;600;700&family=Libre+Baskerville&display=swap">
<style>
  :root {
    --paper: #f7f5f6;
    --leaf: #5aa832;
    --brand-green: #8cc63f;
    --teal: #17888e;
    --body-green: #6aa83a;
    --rule: #a9a4a6;
    --est-grey: #8e8a8c;
  }
  html, body {
    margin: 0;
    padding: 0;
    overflow: hidden;
  }
  .card {
    position: relative;
    width: 849px;
    height: 1200px;
    background: var(--paper);
    overflow: hidden;
    font-family: "Raleway", Arial, sans-serif;
  }
  .collage {
    position: absolute;
    inset: 0;
    width: 849px;
    height: 1200px;
  }
  .masthead {
    position: absolute;
    top: 0;
    left: 333px;
    width: 504px;
    text-align: center;
  }
  .brand-name {
    position: absolute;
    top: 48px;
    left: 0;
    width: 504px;
    margin: 0;
    font-size: 62px;
    font-weight: 400;
    letter-spacing: 8px;
    color: var(--brand-green);
    line-height: 1;
  }
  .established {
    position: absolute;
    top: 127px;
    left: 0;
    width: 504px;
    margin: 0;
    font-family: "Libre Baskerville", Georgia, serif;
    font-size: 19px;
    letter-spacing: 2px;
    color: var(--est-grey);
    line-height: 1;
  }
  .header-divider {
    position: absolute;
    top: 168px;
    left: 0;
    width: 504px;
    height: 18px;
  }
  .thank-you {
    position: absolute;
    top: 200px;
    left: 0;
    width: 504px;
    margin: 0;
    font-size: 44px;
    font-weight: 600;
    letter-spacing: 4px;
    color: var(--teal);
    line-height: 1.1;
  }
  .policy {
    position: absolute;
    right: 34px;
    top: 940px;
    width: 560px;
    text-align: right;
  }
  .policy-title {
    margin: 0 0 10px;
    font-size: 35px;
    font-weight: 600;
    letter-spacing: 3px;
    color: var(--teal);
  }
  .policy-text {
    margin: 0;
    font-size: 24px;
    line-height: 30px;
    font-weight: 500;
    letter-spacing: 0.6px;
    color: var(--body-green);
  }
</style>
</head>
<body>
<main class="card">
  <svg class="collage" viewBox="0 0 849 1200" xmlns="http://www.w3.org/2000/svg">
    <defs>
      <linearGradient id="tone-warm" x1="0" y1="0" x2="1" y2="1">
        <stop offset="0" stop-color="#c9a08a"/>
        <stop offset="1" stop-color="#6e4a3a"/>
      </linearGradient>
      <linearGradient id="tone-blush" x1="0" y1="0" x2="1" y2="1">
        <stop offset="0" stop-color="#e8cfc6"/>
        <stop offset="1" stop-color="#9c6b55"/>
      </linearGradient>
      <linearGradient id="tone-sky" x1="0" y1="0" x2="0" y2="1">
        <stop offset="0" stop-color="#7d6a60"/>
        <stop offset="1" stop-color="#9fb7d8"/>
      </linearGradient>
      <linearGradient id="tone-ivory" x1="0" y1="0" x2="1" y2="1">
        <stop offset="0" stop-color="#eef0f2"/>
        <stop offset="1" stop-color="#b88e74"/>
      </linearGradient>
      <linearGradient id="tone-grey" x1="0" y1="0" x2="1" y2="1">
        <stop offset="0" stop-color="#c7c9cb"/>
        <stop offset="1" stop-color="#a77c62"/>
      </linearGradient>
      <linearGradient id="tone-rose" x1="0" y1="0" x2="0" y2="1">
        <stop offset="0" stop-color="#e6c3c4"/>
        <stop offset="1" stop-color="#b3262a"/>
      </linearGradient>
    </defs>

    <g class="photo-tiles" stroke="var(--leaf)" stroke-width="5" stroke-linejoin="miter">
      <polygon role="img" aria-label="Photo: model wearing a gold statement necklace" fill="url(#tone-warm)"
               points="157,0 314,200 157,400 0,200"/>
      <polygon role="img" aria-label="Photo: model in profile wearing a kundan necklace and earrings" fill="url(#tone-blush)"
               points="314,200 471,400 314,600 157,400"/>
      <polygon role="img" aria-label="Photo: model in a floral off-shoulder dress with a gold choker" fill="url(#tone-sky)"
               points="157,400 314,600 157,800 0,600"/>
      <polygon role="img" aria-label="Photo: model in a white dress with a layered gold necklace" fill="url(#tone-ivory)"
               points="471,400 628,600 471,800 314,600"/>
      <polygon role="img" aria-label="Photo: close-up of model wearing a choker and drop earrings" fill="url(#tone-grey)"
               points="314,600 471,800 314,1000 157,800"/>
      <polygon role="img" aria-label="Photo: model in a red outfit wearing a green-stone necklace" fill="url(#tone-rose)"
               points="157,800 314,1000 157,1200 0,1000"/>
    </g>
  </svg>

  <header class="masthead">
    <h1 class="brand-name">BELLARA</h1>
    <p class="established">EST. 2006</p>
    <svg class="header-divider" viewBox="0 0 504 18" xmlns="http://www.w3.org/2000/svg" aria-hidden="true">
      <line x1="0" y1="9" x2="504" y2="9" stroke="var(--rule)" stroke-width="1.5"/>
      <polygon points="252,4 270,9 252,14 234,9" fill="var(--est-grey)"/>
    </svg>
    <h2 class="thank-you">THANK YOU</h2>
  </header>

  <section class="policy">
    <h3 class="policy-title">POLICY DETAILS</h3>
    <p class="policy-text">
      Lorem ipsum dolor sit amet,<br>
      consectetur adipiscing elit, sed do<br>
      eiusmod tempor incididunt ut labore et<br>
      dolore magna aliqua. Ut enim ad minim<br>
      veniam, quis nostrud exercitation<br>
      ullamco laboris nisi
    </p>
  </section>
</main>
</body>
</html>
```